Bespoke Poems business needs a business card designed

I am a writer that specialises in Bespoke Poems for people for significant life events.
I want a business card that stands out and portrays class and professionalism but is also welcoming & indicates warmth and honesty.
I'm happy with the logo that was designed for me, I would like to see it in raised print on the business card. I am open to suggestions on colours but think perhaps gold or silver writing for the logo would look good. I would like just the logo and my name and contact details on the front of the card. On the back of the card, I would like a list of the different events I provide poems for I will upload a photo of my current business card for reference. My current logo has a shading behind it that I don't like, I just want the words of the logo without any background colour

Target Market(s)

People wanting to provide a unique gift to someone special in their life

Industry/Entity Type

Writer

Contact Information for Business Card

Logo, my name and contact details on the front and a list of all the events I write poetry for on the back

Font styles to use
Script

Requirements
Must have
• I would like to see the logo, if possible, in a raised type of print on the card so that you can feel the actual words. I would like to have a glossy finish to the card and be able to print it on good quality board
Should not have
• The shading that is currently behind the logo on my current business card

```html
<!DOCTYPE html>
<html lang="en">
<head>
<meta charset="UTF-8">
<title>Harbourlight Writing – Business Card</title>
<link href="https://fonts.googleapis.com/css2?family=Great+Vibes&family=Montserrat:wght@400;500;600&display=swap" rel="stylesheet">
<style>
  :root {
    --stage-light: #eef0f3;
    --stage-dark: #c9ced6;
    --card: #2e2e2f;
    --card-edge: #3a3a3b;
    --ink: #f4f4f4;
    --ink-soft: #d9d9d9;
  }
  * { margin: 0; padding: 0; box-sizing: border-box; }
  html, body {
    width: 1200px;
    height: 675px;
    overflow: hidden;
  }
  body {
    background: radial-gradient(ellipse at 40% 60%, var(--stage-light) 0%, var(--stage-dark) 100%);
    font-family: "Montserrat", sans-serif;
    position: relative;
  }
  .card {
    position: absolute;
    top: 182px;
    width: 540px;
    height: 310px;
    background: linear-gradient(160deg, var(--card-edge) 0%, var(--card) 60%);
    border-radius: 4px;
    box-shadow: 0 10px 28px rgba(0, 0, 0, 0.28);
    color: var(--ink);
  }
  .card--front { left: 40px; }
  .card--back { left: 620px; }

  /* Front */
  .brand {
    position: absolute;
    top: 44px;
    left: 60px;
    width: 420px;
    text-align: center;
  }
  .brand__name {
    display: flex;
    align-items: center;
    justify-content: center;
    gap: 12px;
    font-family: "Montserrat", sans-serif;
    font-weight: 500;
    font-size: 30px;
    line-height: 1.2;
    letter-spacing: 1px;
    color: var(--ink);
  }
  .brand__dot {
    width: 12px;
    height: 12px;
    border-radius: 50%;
    background: var(--ink);
  }
  .brand__tagline {
    margin-top: 10px;
    font-size: 15px;
    font-weight: 400;
    letter-spacing: 1px;
    color: var(--ink-soft);
  }
  .contact {
    position: absolute;
    left: 52px;
    top: 178px;
  }
  .contact__name {
    font-size: 22px;
    font-weight: 600;
    margin-bottom: 12px;
  }
  .contact__phone {
    font-size: 15px;
    letter-spacing: 4px;
    margin-bottom: 6px;
  }
  .contact__email {
    font-size: 15px;
    letter-spacing: 0.5px;
  }

  /* Back */
  .events {
    position: absolute;
    left: 40px;
    top: 34px;
    right: 30px;
  }
  .events__title {
    font-family: "Great Vibes", cursive;
    font-size: 29px;
    font-weight: 400;
    margin-bottom: 10px;
  }
  .events__list {
    list-style: none;
    padding-left: 14px;
  }
  .events__item {
    font-size: 19px;
    font-weight: 500;
    line-height: 1.55;
  }
  .events__item::before {
    content: "•";
    margin-right: 8px;
  }
</style>
</head>
<body>
  <section class="card card--front" aria-label="Business card front">
    <div class="brand">
      <div class="brand__name"><span>Harbourlight Writing</span><span class="brand__dot"></span></div>
      <p class="brand__tagline">Bespoke Poems</p>
    </div>
    <div class="contact">
      <p class="contact__name">Daniel Harper</p>
      <p class="contact__phone">0412 555 017</p>
      <p class="contact__email">daniel@harbourlightwriting.com</p>
    </div>
  </section>

  <section class="card card--back" aria-label="Business card back">
    <div class="events">
      <h2 class="events__title">Momentous Life Events Personalised in Poetry</h2>
      <ul class="events__list">
        <li class="events__item">Weddings &amp; Anniversaries</li>
        <li class="events__item">Birthdays &amp; Christmas</li>
        <li class="events__item">Valentines Day</li>
        <li class="events__item">Retirements, Business &amp; Corporate Events</li>
        <li class="events__item">Funerals &amp; Eulogies</li>
      </ul>
    </div>
  </section>
</body>
</html>
```